Kestrel Photography Business Card

I need a business card designed for a photography business based in Perth, Western Australia called Kestrel Photography.

We specialise in wedding, event photography and portrait photography.

The business card must borrow the style of the attached logo.

The hex codes for the colours in the logo are:
#ED1D85 - Pink
#89C23E - Green
#37282F - Black

The name on the card will be:
Name: Toviran
Phone: 0417395268
Website: www.kestrelphotography.com.au
Facebook: kestrelphotography

I am open and happy to accept creative concepts.

I’d like some space at the back for writing notes and appointment details.

```html
<!DOCTYPE html>
<html lang="en">
<head>
<meta charset="utf-8">
<title>Kestrel Photography – Business Card</title>
<link href="https://fonts.googleapis.com/css2?family=Barlow:wght@300;400&display=swap" rel="stylesheet">
<style>
  :root {
    --pink: #ED1D85;
    --green: #89C23E;
    --ink: #37282F;
    --paper: #F1F1F0;
    --rule: #8a8588;
    --backdrop: #E4E2DF;
    --light-text: #ECE8EA;
  }
  * { box-sizing: border-box; margin: 0; padding: 0; }
  html, body {
    width: 1200px; height: 900px; overflow: hidden;
    background: var(--backdrop);
    font-family: "Barlow", Arial, sans-serif;
    font-weight: 300;
  }
  .canvas {
    width: 1200px; height: 900px;
    display: flex; justify-content: center; align-items: center; gap: 80px;
  }
  .card {
    position: relative; width: 340px; height: 556px;
    background: var(--paper);
    box-shadow: 0 10px 30px rgba(55, 40, 47, 0.18);
    overflow: hidden;
  }

  /* front */
  .front-top {
    height: 236px;
    display: flex; flex-direction: column; align-items: center;
    padding-top: 40px;
  }
  .brand-dot {
    width: 40px; height: 40px; border-radius: 50%;
    border: 3px solid var(--pink);
  }
  .brand-name {
    margin-top: 24px; padding-left: 0.5em;
    font-size: 11px; letter-spacing: 0.5em;
    text-transform: uppercase; color: var(--ink);
  }
  .person-name {
    margin-top: 38px;
    font-size: 24px; font-weight: 300; letter-spacing: 0.04em;
    text-transform: uppercase; color: var(--ink);
  }
  .front-bottom {
    position: absolute; left: 0; right: 0; top: 236px; bottom: 0;
    background: var(--ink);
    display: flex; flex-direction: column; justify-content: center;
    gap: 24px;
    padding: 0 74px 0 20px;
  }
  .contact {
    display: flex; flex-direction: column; align-items: center; gap: 6px;
  }
  .contact-label {
    display: flex; align-items: center; gap: 12px;
    color: var(--pink); font-size: 14px; font-weight: 400;
  }
  .contact-label::before, .contact-label::after {
    content: ""; width: 46px; height: 1px; background: var(--pink);
  }
  .contact-value {
    color: var(--light-text); font-size: 15px; letter-spacing: 0.01em;
    white-space: nowrap;
  }

  /* petal fan areas */
  .petal-fan { position: absolute; }
  .front-fan {
    right: 0; top: 74px; width: 62px; height: 170px;
    border-radius: 85px 0 0 85px / 85px 0 0 85px;
    background: linear-gradient(to right, var(--pink) 0%, var(--pink) 45%, var(--green) 100%);
  }
  .back-fan-top {
    top: 0; right: 28px; width: 118px; height: 34px;
    border-radius: 0 0 59px 59px / 0 0 34px 34px;
    background: linear-gradient(to bottom, var(--green) 0%, var(--pink) 70%);
  }
  .back-fan-bottom {
    right: 0; bottom: 0; width: 150px; height: 76px;
    border-top-left-radius: 100% 100%;
    background: radial-gradient(ellipse at 100% 100%, var(--green) 0%, var(--green) 35%, var(--pink) 75%);
  }

  /* back */
  .back-title {
    position: absolute; top: 50px; left: 0; right: 0;
    padding-left: 0.5em; text-align: center;
    font-size: 11px; letter-spacing: 0.5em;
    text-transform: uppercase; color: var(--ink);
  }
  .note-lines {
    position: absolute; top: 112px; left: 34px; right: 34px;
    display: flex; flex-direction: column; gap: 50px;
  }
  .note-line { height: 1px; background: var(--rule); }
</style>
</head>
<body>
<main class="canvas">
  <section class="card card-front">
    <div class="front-top">
      <span class="brand-dot" aria-hidden="true"></span>
      <p class="brand-name">Kestrel Photography</p>
      <h1 class="person-name">Toviran</h1>
    </div>
    <div class="front-bottom">
      <div class="contact">
        <span class="contact-label">phone</span>
        <span class="contact-value">0417395268</span>
      </div>
      <div class="contact">
        <span class="contact-label">web</span>
        <span class="contact-value">www.kestrelphotography.com.au</span>
      </div>
      <div class="contact">
        <span class="contact-label">facebook</span>
        <span class="contact-value">kestrelphotography</span>
      </div>
      <div class="petal-fan front-fan" role="img" aria-label="Pink and green petal fan decoration"></div>
    </div>
  </section>

  <section class="card card-back">
    <div class="petal-fan back-fan-top" role="img" aria-label="Pink and green petal fan decoration"></div>
    <p class="back-title">Kestrel Photography</p>
    <div class="note-lines">
      <div class="note-line"></div>
      <div class="note-line"></div>
      <div class="note-line"></div>
      <div class="note-line"></div>
      <div class="note-line"></div>
      <div class="note-line"></div>
      <div class="note-line"></div>
    </div>
    <div class="petal-fan back-fan-bottom" role="img" aria-label="Pink and green petal fan decoration"></div>
  </section>
</main>
</body>
</html>
```